Business card design for strategy and management consulting company. Would like to have a clean and professional business card, based on the attached logo. The company is a strategy and management consulting company focusing on sustainable business modlels based on economic, social and environmental market opportunities. Preferably the logo should be included on both sides of the design.

Industry/Entity Type

Business

Contact Information for Business Card

Håvard Lilleby, CEO/Management consultant
havard.lilleby@quarvenpartners.example
Mob: +47 948 26 317
Office: Vikfjell gate 14, pb 312 sentrum, N-0172 Oslo Norway

Requirements
Must have
• Include attached logo
Nice to have
• Would like to have the logo on both sides
Should not have
• Many colours.

```html
<!DOCTYPE html>
<html lang="en">
<head>
<meta charset="utf-8">
<title>Quarven – Business Card</title>
<link href="https://fonts.googleapis.com/css2?family=Open+Sans:wght@400;600;700&display=swap" rel="stylesheet">
<style>
  :root {
    --backdrop: #5b4333;
    --card: #161616;
    --wordmark: #5a5b5e;
    --name: #6c6d70;
    --detail: #5f6063;
  }
  * { margin: 0; padding: 0; box-sizing: border-box; }
  html, body {
    width: 1200px;
    height: 1000px;
    overflow: hidden;
  }
  body {
    position: relative;
    background: var(--backdrop);
    font-family: "Open Sans", Arial, sans-serif;
  }
  .card {
    position: absolute;
    left: 266px;
    width: 666px;
    height: 397px;
    background: var(--card);
    box-shadow: 0 4px 14px rgba(0,0,0,0.45);
  }
  .card--front { top: 74px; }
  .card--back { top: 533px; }

  .company-name {
    position: absolute;
    color: var(--wordmark);
    font-weight: 600;
    line-height: 1;
    white-space: nowrap;
  }
  .card--front .company-name {
    left: 0;
    right: 0;
    text-align: center;
    top: 150px;
    font-size: 92px;
  }
  .card--back .company-name {
    left: 32px;
    top: 62px;
    font-size: 62px;
  }

  .contact {
    position: absolute;
    left: 33px;
    top: 224px;
    color: var(--detail);
  }
  .contact__name {
    font-size: 19px;
    font-weight: 700;
    letter-spacing: 0.5px;
    color: var(--name);
    text-transform: uppercase;
    line-height: 30px;
  }
  .contact__role {
    font-size: 15.5px;
    line-height: 24px;
    margin-bottom: 20px;
  }
  .contact__line {
    font-size: 15.5px;
    line-height: 28px;
    display: flex;
    align-items: center;
    white-space: nowrap;
  }
  .contact__sep {
    width: 6px;
    height: 6px;
    border-radius: 50%;
    background: var(--detail);
    margin: 0 10px;
  }
</style>
</head>
<body>
  <section class="card card--front">
    <p class="company-name">Quarven</p>
  </section>

  <section class="card card--back">
    <p class="company-name">Quarven</p>
    <div class="contact">
      <p class="contact__name">Håvard Lilleby</p>
      <p class="contact__role">CEO / Management consultant</p>
      <p class="contact__line">+47 948 26 317<span class="contact__sep"></span>havard.lilleby@quarvenpartners.example</p>
      <p class="contact__line">Vikfjell gate 14, pb 312 sentrum, 0172 Oslo Norway</p>
    </div>
  </section>
</body>
</html>
```